Invitation to Retail Shopping Event

-Must include logo
-Can contain product pictures depending on design
-I prefer any graphics to be my own product pictures
-Should include the following language:
Sip and Shop
Thursday, November 18
11 to 1 pm
478 Fenwick Lane
Come enjoy sips, snacks and shopping! Be the first to preview our new winter collection and get an early start on your holiday gifting.
Please RSVP to 402-319-5577 or info@pelbrika.com

```html
<!DOCTYPE html>
<html lang="en">
<head>
<meta charset="utf-8">
<title>Pelbrika – Sip and Shop Invitation</title>
<link rel="stylesheet" href="https://fonts.googleapis.com/css2?family=Questrial&family=Didact+Gothic&family=Montserrat:wght@400&display=swap">
<style>
  :root {
    --stage: #000000;
    --card-border: #ffffff;
    --blush: #ecd1ca;
    --ink: #555555;
    --white: #ffffff;
    --photo-gold: #b58f5c;
    --photo-lilac: #b9a4b4;
    --photo-jewel: #d8bb7a;
  }
  * { margin: 0; padding: 0; box-sizing: border-box; }
  html, body {
    width: 1200px; height: 1200px; overflow: hidden;
    background: var(--stage);
  }
  .invitation {
    position: absolute; left: 342px; top: 219px;
    width: 516px; height: 761px;
    background: var(--card-border);
    padding: 12px;
  }
  .invitation__panel {
    position: relative; width: 100%; height: 100%;
    background: var(--blush); overflow: hidden;
    font-family: "Questrial", sans-serif; color: var(--white);
    text-align: center;
  }
  .corner-pattern { position: absolute; }
  .corner-pattern--top { left: 0; top: 0; width: 214px; height: 134px; }
  .corner-pattern--bottom { right: 0; bottom: 0; width: 214px; height: 138px; }
  .brand-name {
    position: absolute; left: 0; right: 0; top: 158px;
    font-family: "Questrial", sans-serif;
    font-size: 46px; letter-spacing: 3px; color: var(--ink);
  }
  .event-title {
    position: absolute; left: 0; right: 0; top: 273px;
    font-size: 40px; font-weight: 400; letter-spacing: -0.5px;
  }
  .event-details {
    position: absolute; left: 0; right: 0; top: 337px;
    font-size: 15px; font-weight: 700; line-height: 20px;
  }
  .event-details .address { margin-top: 7px; }
  .event-message {
    position: absolute; left: 0; right: 0; top: 442px;
    font-family: "Didact Gothic", sans-serif;
    font-size: 17px; line-height: 25px;
  }
  .product-row {
    position: absolute; left: 0; right: 0; top: 552px;
    display: flex; justify-content: center; gap: 27px;
  }
  .product-circle {
    width: 72px; height: 72px; border-radius: 50%;
    background: var(--white);
    display: flex; align-items: center; justify-content: center;
  }
  .product-photo { border-radius: 50%; }
  .product-photo--tray { width: 44px; height: 30px; background: radial-gradient(var(--photo-gold), #6e5538); }
  .product-photo--slippers { width: 44px; height: 36px; background: radial-gradient(#e8d8dc, var(--photo-lilac)); }
  .product-photo--earrings { width: 40px; height: 34px; background: radial-gradient(#f3e6c4, var(--photo-jewel)); }
  .rsvp {
    position: absolute; left: 30px; top: 679px;
    font-family: "Montserrat", sans-serif; font-size: 11.5px;
    line-height: 18px; text-align: left;
  }
</style>
</head>
<body>
  <main class="invitation">
    <div class="invitation__panel">
      <svg class="corner-pattern corner-pattern--top" role="img" aria-label="White leopard-spot pattern in the top left corner" viewBox="0 0 214 134">
        <defs>
          <linearGradient id="spotsTop" x1="0" y1="0" x2="1" y2="1">
            <stop offset="0" stop-color="#ffffff" stop-opacity="0.85"/>
            <stop offset="1" stop-color="#ffffff" stop-opacity="0"/>
          </linearGradient>
        </defs>
        <polygon points="0,0 214,0 0,134" fill="url(#spotsTop)"/>
      </svg>

      <div class="brand-name">PELBRIKA</div>

      <h1 class="event-title">Sip and Shop</h1>
      <div class="event-details">
        <p>Thursday, November 18</p>
        <p>11 to 1 pm</p>
        <p class="address">478 Fenwick Lane</p>
      </div>

      <div class="event-message">
        <p>Come enjoy sips, snacks and shopping !</p>
        <p>Be the first to preview our new winter collection</p>
        <p>and get an early start on your holiday gifting.</p>
      </div>

      <div class="product-row">
        <div class="product-circle"><div class="product-photo product-photo--tray" role="img" aria-label="Leopard print round tray"></div></div>
        <div class="product-circle"><div class="product-photo product-photo--slippers" role="img" aria-label="Lilac fluffy slippers"></div></div>
        <div class="product-circle"><div class="product-photo product-photo--earrings" role="img" aria-label="Gold flower stud earrings"></div></div>
      </div>

      <div class="rsvp">
        <p>Please RSVP to 402-319-5577</p>
        <p>or info@pelbrika.com</p>
      </div>

      <svg class="corner-pattern corner-pattern--bottom" role="img" aria-label="White leopard-spot pattern in the bottom right corner" viewBox="0 0 214 138">
        <defs>
          <linearGradient id="spotsBottom" x1="1" y1="1" x2="0" y2="0">
            <stop offset="0" stop-color="#ffffff" stop-opacity="0.85"/>
            <stop offset="1" stop-color="#ffffff" stop-opacity="0"/>
          </linearGradient>
        </defs>
        <polygon points="214,0 214,138 0,138" fill="url(#spotsBottom)"/>
      </svg>
    </div>
  </main>
</body>
</html>
```